2020 Brambleton Summer Camp Brochure

We are wanting to design a brochure to be used for our Christian Summer Camp. This brochure will be used to attract new campers and current campers. We would like for it to be fun and exciting. It will be 11 x 8.5 folded. It could be either in portrait or landscape format. We have uploaded a document that has all the information that will need to be included. Also, we have uploaded several pictures that can be used. We would love for the back cover to have a design for our theme (see information sheet for more details).

Target Market(s)

Ages 8 - 18 and parents

Colors

Designer to choose colors to be used in the design.

Requirements
Must have
• The information included in document.
Nice to have
• Design for our theme on back

```html
<!DOCTYPE html>
<html lang="en">
<head>
<meta charset="utf-8">
<title>Camp Brambleton Summer Camp Brochure 2020</title>
<link href="https://fonts.googleapis.com/css2?family=Montserrat:wght@400;500;600;700;800&display=swap" rel="stylesheet">
<style>
  :root {
    --teal-dark: #1d5b60;
    --teal: #3e9aa3;
    --teal-light: #bfe3e6;
    --water: #58c3d2;
    --green: #6cc04a;
    --green-deep: #2f9a3a;
    --green-pale: #d6efc8;
    --ink: #444;
    --footer: #4b4b4b;
    --paper: #ffffff;
    --backdrop: #dcdcdc;
  }
  * { box-sizing: border-box; margin: 0; padding: 0; }
  html, body { width: 672px; height: 1200px; overflow: hidden; }
  body { background: var(--backdrop); font-family: "Montserrat", sans-serif; position: relative; }

  .sheet { position: absolute; background: var(--paper); overflow: hidden; box-shadow: 0 6px 18px rgba(0,0,0,.18); }
  .sheet--outer { left: 60px; top: 22px; width: 440px; height: 550px; }
  .sheet--inner { left: 175px; top: 615px; width: 470px; height: 565px; }

  /* ---------- mailer panel (printed upside down for folding) ---------- */
  .mailer { position: absolute; left: 0; top: 0; width: 440px; height: 270px; transform: rotate(180deg); overflow: hidden;
    background: linear-gradient(180deg, #e6f4f5 0%, var(--teal-light) 35%, var(--teal) 70%, var(--teal-dark) 100%); }
  .mailer__scene { position: absolute; inset: 0;
    background: linear-gradient(180deg, #e9f6f8 0%, #a9dde3 30%, var(--water) 52%, #7bc6d0 70%, #3c8d96 100%); }
  .mailer__halo { position: absolute; left: -120px; top: 90px; width: 420px; height: 420px; border-radius: 50%;
    background: rgba(255,255,255,.55); }
  .mailer__halo::after { content: ""; position: absolute; inset: 14px; border-radius: 50%; background: rgba(255,255,255,.7); }
  .contact { position: absolute; left: 40px; top: 92px; width: 200px; color: var(--teal-dark); }
  .contact__name { font-weight: 800; font-size: 17px; line-height: 1; text-align: center; letter-spacing: .5px; }
  .contact__rule { width: 60px; height: 2px; background: var(--green-deep); margin: 6px 0 6px 66px; }
  .contact__line { display: flex; align-items: center; gap: 6px; font-size: 8.5px; font-weight: 500; margin-bottom: 5px; }
  .contact__line svg { width: 10px; height: 10px; flex: none; }
  .contact__line--phone { font-size: 11px; }
  .contact__web { font-size: 9px; font-weight: 700; color: var(--green-deep); letter-spacing: .6px; margin-top: 2px; }
  .address-box { position: absolute; left: 244px; top: 12px; width: 186px; height: 246px; background: var(--paper); }
  .address-box__resident { position: absolute; left: 0; right: 0; top: 128px; text-align: center; font-size: 6px; color: #333; letter-spacing: .3px; }
  .indicia { position: absolute; right: 12px; top: 8px; width: 50px; height: 62px; border: .7px solid #333;
    font-size: 4px; line-height: 1.6; text-align: center; padding-top: 8px; color: #222; }
  .indicia strong { font-size: 5px; font-weight: 600; }

  /* ---------- front cover ---------- */
  .cover { position: absolute; left: 0; top: 270px; width: 440px; height: 280px; overflow: hidden; }
  .cover__photo { position: absolute; inset: 0;
    background: radial-gradient(ellipse at 70% 25%, #e88c8c 0 14%, transparent 30%),
                linear-gradient(135deg, #8a6f55 0%, #a98c6e 35%, #7d6650 65%, #5e4b3b 100%); }
  .cover__arc { position: absolute; left: 110px; top: 128px; width: 560px; height: 560px; border-radius: 50%;
    background: var(--paper); box-shadow: 0 0 0 9px rgba(255,255,255,.45); }
  .cover__title { position: absolute; right: 14px; top: 186px; text-align: left; color: var(--teal-dark); font-weight: 800; }
  .cover__title .line { display: block; font-size: 33px; line-height: .86; letter-spacing: .5px; }
  .cover__title .line--first { margin-left: 10px; }
  .cover__tag { position: absolute; right: 15px; top: 252px; display: flex; align-items: center; gap: 7px;
    color: var(--green); font-weight: 800; font-size: 19px; letter-spacing: .8px; }
  .cover__tag::before { content: ""; width: 100px; height: 2px; background: var(--green-deep); }

  /* ---------- inner spread ---------- */
  .inner__photo { position: absolute; left: 0; top: 0; width: 470px; height: 290px;
    background: linear-gradient(160deg, #9bbf7c 0%, #6f9c6a 28%, #4a6f97 50%, #c7d3dc 72%, #e2e6ea 100%); }
  .inner__veil { position: absolute; left: -220px; top: -300px; width: 530px; height: 600px; border-radius: 50%;
    background: rgba(255,255,255,.8); }
  .inner__fade { position: absolute; left: 0; top: 170px; width: 470px; height: 130px;
    background: linear-gradient(180deg, rgba(255,255,255,0) 0%, rgba(255,255,255,.9) 70%, #fff 100%); }
  .headline { position: absolute; left: 30px; top: 18px; color: var(--teal-dark); font-weight: 800; font-size: 18.5px; line-height: 1.06; letter-spacing: .4px; }
  .intro { position: absolute; left: 29px; top: 124px; width: 200px; color: var(--green-deep); font-weight: 600; font-size: 9.3px; line-height: 1.3; }
  .intro::after { content: ""; display: block; width: 105px; height: 1.5px; background: var(--green-deep); margin-top: 3px; }
  .activities { position: absolute; left: 30px; top: 207px; }
  .activities__title { color: var(--teal-dark); font-weight: 700; font-size: 11.5px; line-height: 1.28; letter-spacing: .4px; }
  .activities__title em { font-style: normal; color: var(--green); }
  .activities__list { list-style: none; margin-top: 2px; color: var(--ink); font-size: 9.8px; line-height: 14.6px; letter-spacing: .3px; }
  .bubble { position: absolute; width: 110px; height: 110px; border-radius: 50%; box-shadow: 0 0 0 6px var(--green-pale); }
  .bubble--blob { left: 210px; top: 207px; background: linear-gradient(180deg, #4f7d3e 0%, #6f8f5a 45%, #5d7a70 100%); }
  .bubble--horse { left: 329px; top: 207px; background: linear-gradient(180deg, #4e7b3e 0%, #7ea662 55%, #5a4434 100%); }
  .bubble--foam { left: 22px; top: 419px; background: linear-gradient(180deg, #3e5e36 0%, #d9dcdc 45%, #f2f2f2 75%, #8a8d8e 100%); }
  .sessions__title { position: absolute; left: 146px; top: 318px; color: var(--teal-dark); font-weight: 700; font-size: 17px; letter-spacing: .6px; }
  .schedule { position: absolute; left: 144px; top: 339px; width: 311px; height: 170px; }
  .schedule svg.bg { position: absolute; inset: 0; }
  .schedule__side { position: absolute; left: 2px; top: 85px; transform: translate(-50%,-50%) rotate(-90deg); transform-origin: center; white-space: nowrap; color: #e9f7e2; text-align: center; }
  .schedule__ages { position: absolute; left: 8px; top: 100px; transform: translate(-50%,-50%) rotate(-90deg); font-size: 7px; font-weight: 600; color: #fff; white-space: nowrap; }
  .schedule__types { position: absolute; left: 17px; top: 85px; transform: translate(-50%,-50%) rotate(-90deg); font-size: 5.6px; font-weight: 500; color: var(--teal-dark); white-space: nowrap; }
  .schedule__rows { position: absolute; left: 27px; top: 10px; right: 10px; list-style: none; }
  .schedule__row { display: flex; height: 15.4px; align-items: center; font-size: 8px; }
  .schedule__name { width: 143px; color: #fff; font-weight: 700; letter-spacing: .2px; }
  .schedule__name span { font-weight: 400; font-size: 7px; margin-left: 4px; color: #eafbe0; }
  .schedule__dates { width: 98px; color: #333; letter-spacing: .2px; }
  .schedule__price { flex: 1; text-align: right; color: #333; }
  .register { position: absolute; left: 0; right: 0; bottom: 0; height: 44px; background: var(--footer);
    display: flex; align-items: center; justify-content: center; color: var(--green); font-weight: 800; font-size: 16.5px; letter-spacing: .4px; padding-bottom: 6px; }
</style>
</head>
<body>

<!-- Outside sheet: mailer panel and front cover -->
<section class="sheet sheet--outer">
  <div class="mailer">
    <div class="mailer__scene" role="img" aria-label="Photo of a wooden cross standing over lake water reflecting clouds"></div>
    <div class="mailer__halo"></div>
    <div class="contact">
      <p class="contact__name">CAMP<br>BRAMBLETON</p>
      <div class="contact__rule"></div>
      <p class="contact__line">
        <svg viewBox="0 0 10 10"><path d="M5 1C3.2 1 2 2.3 2 4c0 2.2 3 5 3 5s3-2.8 3-5C8 2.3 6.8 1 5 1z" fill="none" stroke="currentColor" stroke-width=".8"/><circle cx="5" cy="4" r="1" fill="none" stroke="currentColor" stroke-width=".7"/></svg>
        PO Box 4821, Millbrook, AR
      </p>
      <p class="contact__line contact__line--phone">
        <svg viewBox="0 0 10 10"><path d="M2.5 1.5l1.5 0 .8 2-1 .8c.5 1.1 1.2 1.8 2.3 2.3l.8-1 2 .8v1.5c0 .5-.4.8-.9.8C4.8 8.5 1.5 5.2 1.5 2.4c0-.5.4-.9 1-.9z" fill="none" stroke="currentColor" stroke-width=".7"/></svg>
        501-555-0142
      </p>
      <p class="contact__line">
        <svg viewBox="0 0 10 10"><path d="M1 3l8-2-2 8-2-3-4-3z M5 6l4-5" fill="none" stroke="currentColor" stroke-width=".7" stroke-linejoin="round"/></svg>
        office@campbrambleton.org
      </p>
      <p class="contact__web">WWW.CAMPBRAMBLETON.ORG</p>
    </div>
    <div class="address-box">
      <div class="indicia">NON-PROFIT ORG<br>U.S. POSTAGE<br><strong>PAID</strong><br>MILLBROOK, AR<br>PERMIT #70</div>
      <p class="address-box__resident">OR CURRENT RESIDENT</p>
    </div>
  </div>

  <div class="cover">
    <div class="cover__photo" role="img" aria-label="Photo of a young camper drawing a bow at archery with a helper's hands guiding the arrow"></div>
    <div class="cover__arc"></div>
    <h1 class="cover__title"><span class="line line--first">CAMP</span><span class="line">BRAMBLETON</span></h1>
    <p class="cover__tag">SUMMER CAMP</p>
  </div>
</section>

<!-- Inside spread -->
<section class="sheet sheet--inner">
  <div class="inner__photo" role="img" aria-label="Photo of cheering campers in life jackets on a raft at the lake"></div>
  <div class="inner__veil"></div>
  <div class="inner__fade"></div>

  <h2 class="headline">EXPERIENCE SUMMER<br>LIKE<br>NEVER BEFORE<br>AT CAMP<br>BRAMBLETON!</h2>
  <p class="intro">Join us for a summer you will never forget! Experience God in a new way. Create life-long friendships.</p>

  <div class="activities">
    <h3 class="activities__title">PARTICIPATE<br>IN OUR <em>AWESOME</em><br>ACTIVITIES:</h3>
    <ul class="activities__list">
      <li>Archery Tag</li><li>Blob</li><li>Rappelling</li><li>Water Trampoline</li><li>Horses</li>
      <li>Archery</li><li>Air Rifles</li><li>Fishing</li><li>Hiking</li><li>Arts and Crafts</li><li>and much more!</li>
    </ul>
  </div>

  <div class="bubble bubble--blob" role="img" aria-label="Photo of a camper jumping off the blob into the lake"></div>
  <div class="bubble bubble--horse" role="img" aria-label="Photo of a camper riding a paint horse"></div>
  <div class="bubble bubble--foam" role="img" aria-label="Photo of campers covered in shaving foam during a game"></div>

  <h3 class="sessions__title">SESSIONS 2020</h3>
  <div class="schedule">
    <svg class="bg" viewBox="0 0 311 170" preserveAspectRatio="none">
      <defs>
        <linearGradient id="leaf" x1="0" y1="0" x2="1" y2="0">
          <stop offset="0" stop-color="#5fb43f"/><stop offset="1" stop-color="#7fcb5a"/>
        </linearGradient>
      </defs>
      <rect width="311" height="170" fill="#dbf1cf"/>
      <path d="M0 0H180C160 40 155 120 175 170H0Z" fill="url(#leaf)"/>
      <path d="M180 0C160 40 155 120 175 170" fill="none" stroke="#bfe5ac" stroke-width="6"/>
    </svg>
    <span class="schedule__ages">Ages 8 - 18</span>
    <span class="schedule__types">11-Day Sessions/7-Day Sessions/4-Day Session</span>
    <ul class="schedule__rows">
      <li class="schedule__row"><span class="schedule__name">Session 1<span>(7-Day)</span></span><span class="schedule__dates">May 31 - June 06</span><span class="schedule__price">$285</span></li>
      <li class="schedule__row"><span class="schedule__name">Short Session 1<span>(4-Day)</span></span><span class="schedule__dates">May 31 - June 03</span><span class="schedule__price">$180</span></li>
      <li class="schedule__row"><span class="schedule__name">Session 2<span>(11-Day)</span></span><span class="schedule__dates">June 07 - June 18</span><span class="schedule__price">$425</span></li>
      <li class="schedule__row"><span class="schedule__name">Session 2B<span>(7-Day)</span></span><span class="schedule__dates">June 07 - June 13</span><span class="schedule__price">$285</span></li>
      <li class="schedule__row"><span class="schedule__name">Session 3<span>(11-Day)</span></span><span class="schedule__dates">June 28 - July 09</span><span class="schedule__price">$425</span></li>
      <li class="schedule__row"><span class="schedule__name">Session 3B<span>(7-Day)</span></span><span class="schedule__dates">June 28 - July 04</span><span class="schedule__price">$285</span></li>
      <li class="schedule__row"><span class="schedule__name">Session 4<span>(11-Day)</span></span><span class="schedule__dates">July 12 - July 23</span><span class="schedule__price">$425</span></li>
      <li class="schedule__row"><span class="schedule__name">Session 4B<span>(7-Day)</span></span><span class="schedule__dates">July 12 - July 18</span><span class="schedule__price">$285</span></li>
      <li class="schedule__row"><span class="schedule__name">Session 5<span>(7-Day)</span></span><span class="schedule__dates">July 26 - August 01</span><span class="schedule__price">$285</span></li>
      <li class="schedule__row"><span class="schedule__name">Short Session 2<span>(4-Day)</span></span><span class="schedule__dates">July 26 - July 29</span><span class="schedule__price">$180</span></li>
    </ul>
  </div>

  <p class="register">Register today at campbrambleton.org!</p>
</section>

</body>
</html>
```